Brochure for The Riverside Lantern Club Private Venue

Brochure to sell the venue and food & beverage services for private parties
Venue name is The Riverside Lantern Club

Target Market(s)

Age: 25 - 40 female

Industry/Entity Type

Events

Requirements
Must have
• Please also put the venue name, address, website and phone
• Riverside Lantern Club
• 4718 Marigold Crest Blvd
• National City, CA 91950
• RiversideLantern.Club
• (858) 555-0193
• TONS of photos. You can grab more photos if needed on the website
Nice to have
• Festive Vibe -

```html
<!DOCTYPE html>
<html lang="en">
<head>
<meta charset="utf-8">
<title>The Riverside Lantern Club — Private Venue Brochure</title>
<link rel="stylesheet" href="https://fonts.googleapis.com/css2?family=Montserrat:wght@700;800;900&family=Arimo:wght@400;700&display=swap">
<style>
:root{
  --stage:#dcdbde;
  --ink:#111;
  --night:#050505;
  --gold:#f2c31a;
  --plum:#6a0f6e;
  --magenta:#d6297f;
  --pink-soft:#f7d6e9;
  --pink-mid:#ea86bd;
  --paper:#ffffff;
  --title:'Montserrat',sans-serif;
  --body:'Arimo',sans-serif;
}
*{box-sizing:border-box;margin:0;padding:0}
html,body{width:807px;height:1200px;overflow:hidden;background:var(--stage)}
body{position:relative;font-family:var(--body);color:var(--ink)}
.spread{position:absolute;left:18px;width:770px;height:495px;display:flex;box-shadow:0 10px 28px rgba(0,0,0,.22)}
.spread--outside{top:55px}
.spread--inside{top:640px}
.page{position:relative;width:385px;height:495px;overflow:hidden}
.photo{position:absolute}
.ragged{position:absolute;left:0;width:100%;display:block}

/* back cover */
.back{background:var(--night)}
.back .photo--exterior{left:0;top:0;width:385px;height:300px;background:linear-gradient(160deg,#1b2252 0%,#3d4fa0 35%,#c6b59a 55%,#4b3a2c 75%,#1d1a2a 100%)}
.thumb-row{position:absolute;left:0;top:300px;width:385px;height:82px;display:flex;border-top:2px solid var(--gold);border-bottom:2px solid var(--gold)}
.thumb-row .photo{position:relative;flex:1;border-left:2px solid var(--gold)}
.thumb-row .photo:first-child{border-left:0}
.thumb--a{background:linear-gradient(140deg,#e6dcc6,#7b5a3d)}
.thumb--b{background:linear-gradient(140deg,#6a5a3c,#d8c9a4 60%,#3b2e22)}
.thumb--c{background:linear-gradient(140deg,#18224e,#5a6bd4 55%,#20284a)}
.back-contact{position:absolute;left:0;top:398px;width:100%;text-align:center;color:var(--gold)}
.venue-name{font-family:var(--title);font-weight:800;color:var(--gold);letter-spacing:.5px}
.back-contact .venue-name{font-size:19px;margin-bottom:8px}
.back-contact .phone{font-size:18px;font-weight:700;margin-bottom:4px}
.back-contact p{font-size:10px;line-height:1.35}

/* front cover */
.front{background:var(--paper)}
.front-title{position:absolute;right:22px;top:52px;text-align:right;font-family:var(--title);font-weight:900;line-height:1}
.front-title .line-1{font-size:27px;color:var(--plum)}
.front-title .line-2{font-size:25px;color:var(--magenta);margin-top:2px}
.front-title .line-3{font-size:11.5px;color:var(--plum);margin-top:6px;letter-spacing:.2px}
.front .photo--table{left:0;top:150px;width:385px;height:250px;background:linear-gradient(125deg,#1f2d6e 0%,#5b74c9 30%,#f2c79b 48%,#aeb6d6 65%,#203071 100%)}
.front-base{position:absolute;left:0;top:400px;width:100%;height:95px;background:var(--night)}
.front-base .venue-name{position:absolute;right:24px;bottom:28px;font-size:18px}

/* inside left */
.inside-left{background:linear-gradient(180deg,#fff 0%,#fff 45%,var(--pink-soft) 65%,var(--pink-mid) 100%)}
.inside-left .photo--hall{left:0;top:0;width:385px;height:240px;background:linear-gradient(150deg,#2a2a2e 0%,#dcdde2 25%,#8b5a3b 55%,#f1d7e3 80%,#e9e9ee 100%)}
.intro{position:absolute;left:22px;top:250px;width:340px;font-size:13px;line-height:1.25;color:var(--plum)}
.tab{position:absolute;font-family:var(--body);font-weight:700;font-size:10px;color:#fff;background:var(--plum);padding:4px 14px;border-radius:0 10px 10px 0;z-index:2}
.card{position:absolute;background:#fff;border-radius:0 0 16px 0;box-shadow:0 1px 3px rgba(0,0,0,.25);font-size:8px;line-height:1.4;padding:12px 10px 8px 12px}
.card ul{padding-left:10px}
.tab--features{left:14px;top:304px}
.card--features{left:20px;top:315px;width:225px;height:84px}
.tab--food{left:14px;top:408px}
.card--food{left:20px;top:419px;width:225px;height:68px}
.tab--buyout{right:18px;top:352px;background:var(--magenta);border-radius:10px 0 0 0;width:120px;text-align:center;line-height:1.15;padding:4px 6px}
.card--buyout{right:18px;top:376px;width:120px;height:92px}

/* inside right */
.inside-right{background:linear-gradient(180deg,var(--pink-mid) 0%,var(--pink-soft) 30%,#fff 60%)}
.menus-title{position:absolute;left:22px;top:18px;font-family:var(--title);font-weight:900;font-size:30px;color:var(--plum)}
.menu{position:absolute;left:22px;top:56px;width:250px;font-size:7.5px;line-height:1.22}
.menu h3{font-family:var(--body);font-weight:700;font-size:8.5px;margin-top:5px}
.menu h3:first-child{margin-top:0}
.menu ul{padding-left:12px}
.menu ol{padding-left:14px}
.menu .note{font-size:6px;line-height:1.25;margin-top:4px}
.dish{position:absolute;right:14px;width:88px;height:58px;border-radius:10px 0 10px 0}
.dish--1{top:60px;background:linear-gradient(135deg,#f4e4df,#c2281f 60%,#7c1b15)}
.dish--2{top:128px;background:linear-gradient(135deg,#fff,#3f7a2a 40%,#e6782a 70%,#3d2618)}
.dish--3{top:196px;background:linear-gradient(135deg,#f1a03a,#9e2c26 50%,#4b2b1a)}
.dish--4{top:264px;background:linear-gradient(135deg,#1d2b6c,#6c86d6 50%,#16204a)}
.inside-right .photo--service{left:0;top:388px;width:385px;height:107px;background:linear-gradient(110deg,#2c2c30 0%,#e07a2b 25%,#f3f0f0 55%,#1f2b4b 85%)}
</style>
</head>
<body>

<section class="spread spread--outside">
  <article class="page back">
    <div class="photo photo--exterior" role="img" aria-label="Night view of the club entrance with blue uplighting"></div>
    <div class="thumb-row">
      <div class="photo thumb--a" role="img" aria-label="Long banquet table set with linen"></div>
      <div class="photo thumb--b" role="img" aria-label="Candlelit table setting"></div>
      <div class="photo thumb--c" role="img" aria-label="Dining room with blue lighting"></div>
    </div>
    <div class="back-contact">
      <div class="venue-name">Riverside Lantern Club</div>
      <div class="phone">(858) 555-0193</div>
      <p>4718 Marigold Crest Blvd, National City, CA 91950</p>
      <p>events@lanternclubcatering.net | RiversideLantern.Club</p>
    </div>
  </article>

  <article class="page front">
    <h1 class="front-title">
      <div class="line-1">BIRTHDAY PARTY,</div>
      <div class="line-2">BABY SHOWER,</div>
      <div class="line-3">CELEBRATION OF LIFE, OR QUINCENIRA</div>
    </h1>
    <div class="photo photo--table" role="img" aria-label="Table with peach roses and glassware under blue light"></div>
    <svg class="ragged" style="top:145px" width="385" height="40" viewBox="0 0 385 40" aria-hidden="true"><path fill="#fff" d="M0 0H385V22L370 30 352 18 330 34 300 14 270 26 250 8 220 20 190 10 150 16 120 6 90 14 60 4 30 12 0 6Z"/></svg>
    <svg class="ragged" style="top:372px" width="385" height="30" viewBox="0 0 385 30" aria-hidden="true"><path fill="#050505" d="M0 30V12L20 6 45 16 70 4 100 14 130 8 160 18 190 6 225 16 260 10 290 20 320 8 350 18 385 10V30Z"/></svg>
    <div class="front-base"><div class="venue-name">Riverside Lantern Club</div></div>
  </article>
</section>

<section class="spread spread--inside">
  <article class="page inside-left">
    <div class="photo photo--hall" role="img" aria-label="Event hall with wooden tables, pink linens and white balloons"></div>
    <svg class="ragged" style="top:212px" width="385" height="34" viewBox="0 0 385 34" aria-hidden="true"><path fill="#fff" d="M0 34V14L25 20 50 8 80 18 110 6 140 16 175 10 205 22 240 12 270 24 300 14 330 26 360 16 385 22V34Z"/></svg>
    <p class="intro">The Riverside Lantern Club is a private event venue and club located 5 minutes south of downtown San Diego in National City</p>

    <div class="tab tab--features">FEATURES</div>
    <div class="card card--features">
      <ul>
        <li>Up to 200 guests</li>
        <li>Full bar options available from 6am to 1:30am</li>
        <li>Plenty of free street parking</li>
        <li>Near Trolley Station</li>
        <li>Includes tables and chairs for up to 150</li>
        <li>In house food and beverage</li>
      </ul>
    </div>

    <div class="tab tab--food">FOOD PRICE</div>
    <div class="card card--food">
      <ul>
        <li>$20++ per person (based on a minimum of 100 guests)</li>
        <li>$23++ per person (based on a minimum of 50 guests)</li>
        <li>$25++ per person (based on a minimum of 25 guests)</li>
      </ul>
    </div>

    <div class="tab tab--buyout">Private Venue<br>Buy-Out Price*</div>
    <div class="card card--buyout">
      <ul>
        <li>$250 rental on Monday through Thursday</li>
        <li>$500 rental on Friday and Sunday</li>
        <li>$1000 rental on Saturday</li>
      </ul>
    </div>
  </article>

  <article class="page inside-right">
    <h2 class="menus-title">MENUS</h2>
    <div class="menu">
      <h3>SELF SERVE FULL MEAL BUFFET</h3>
      <ul>
        <li>Bountiful buffet with rolls, butter, salad, pasta chicken entree, and brownies</li>
        <li>Includes bamboo plates, stainless steel flatware, and linen napkins</li>
      </ul>
      <h3>SELF SERVE FOOD STATION</h3>
      <div>(Pick combination of any 2 stations)</div>
      <ul>
        <li>Mac &amp; Cheese Station</li>
        <li>Asian Stir Fry Noodle Station</li>
        <li>Mashed Potato Bar</li>
        <li>Italian Pasta Station</li>
        <li>Shaken not Stirred Martini Salad Station</li>
        <li>Artisan Slider Bar</li>
        <li>Baja Taco Bar</li>
      </ul>
      <h3>SELF SERVE BRUNCH</h3>
      <ul>
        <li>Fresh whole fruit</li>
        <li>Assorted pastries</li>
        <li>Egg frittata</li>
        <li>Roasted potatoes</li>
        <li>Sausage link</li>
        <li>Chicken entree (add $5pp)</li>
        <li>Champagne Mimosas ($2 each)</li>
      </ul>
      <h3>BEVERAGE PRICE**</h3>
      <ol>
        <li>Herb Infused Water Bar Complimentary</li>
        <li>Coffee, Tea, Iced Tea, Soda $2 per selection</li>
        <li>Beer / Wine / Champagne free flowing for 3 hours - $19.95 pp</li>
        <li>Full Open Bar for 3 hours - $25.25 pp</li>
      </ol>
      <p class="note">*Must utilize all food and beverage service through Riverside Lantern Club<br>** Not including minimal staffing and 18% service charge<br>** Outside beverages not allowed<br>Decor is not included<br>Please ask us for any restrictions that may apply</p>
    </div>
    <div class="photo dish dish--1" role="img" aria-label="Tomato bruschetta bites"></div>
    <div class="photo dish dish--2" role="img" aria-label="Plated entree with vegetables"></div>
    <div class="photo dish dish--3" role="img" aria-label="Buffet of tacos and salsa"></div>
    <div class="photo dish dish--4" role="img" aria-label="Evening table setting"></div>
    <div class="photo photo--service" role="img" aria-label="Server offering appetizers from a catering table"></div>
    <svg class="ragged" style="top:382px" width="385" height="28" viewBox="0 0 385 28" aria-hidden="true"><path fill="#fff" d="M0 0H385V14L360 8 330 20 300 10 270 18 240 6 210 16 180 10 150 20 120 8 90 18 60 10 30 20 0 12Z"/></svg>
  </article>
</section>

</body>
</html>
```